Stonebrook 720 Real Estate Investment Company

We need a business card designed for a real estate investment company named Stonebrook 720. We want to use red#f04a50, orange #f37122 and yellow #fbee3e as the color scheme. The logo colors will need to be modified from the current blue palette. I've attach VitaPathway logo example that captures the color scheme we're going for for Stonebrook 720. Looking for clean Sans Serif fonts.
Contact Information for Business Card
Daniel Furlow
Managing Partner
48317 Whitfield Lane, Suite 510
Tampa, FL 33718
813-555-4870 Mobile
dfurlow@stonebrook720.example
www.stonebrook720.example
Requirements
Must have
- Looking for creative responses.
Nice to have
- Must hit color palette... orange, red, yellow

```html
<!DOCTYPE html>
<html lang="en">
<head>
<meta charset="utf-8">
<title>Stonebrook 720 – Business Card</title>
<link rel="stylesheet" href="https://fonts.googleapis.com/css2?family=Montserrat:wght@400;500;800&display=swap">
<style>
  :root {
    --paper: #ffffff;
    --ink: #060808;
    --brand-red: #f04a50;
    --brand-orange: #f37122;
    --brand-yellow: #fbee3e;
    --text-light: #ffffff;
    --text-dark: #0a0a0a;
  }
  * { margin: 0; padding: 0; box-sizing: border-box; }
  html, body {
    width: 1200px; height: 720px; overflow: hidden;
    background: var(--paper);
    font-family: "Montserrat", Arial, sans-serif;
  }
  .card {
    position: relative; width: 1200px; height: 720px;
    background: var(--paper); overflow: hidden;
  }
  .brand {
    position: absolute; left: 0; top: 0; width: 1200px; height: 372px;
    display: flex; align-items: center; justify-content: center; gap: 28px;
    padding-top: 20px;
  }
  .brand-name {
    font-weight: 800; font-size: 76px; letter-spacing: -1.5px;
    color: var(--brand-red); line-height: 1;
  }
  .brand-mark {
    width: 64px; height: 64px; border-radius: 50%;
    background: var(--brand-orange);
  }
  .info-band {
    position: absolute; left: 0; top: 372px; width: 1200px; height: 348px;
    background: var(--ink);
  }
  .name-plate {
    position: absolute; left: 0; top: 472px; width: 530px; height: 105px;
    background: var(--brand-yellow); color: var(--text-dark);
    padding: 9px 0 0 110px;
  }
  .person-name { font-weight: 400; font-size: 46px; line-height: 1.08; }
  .person-title { font-weight: 400; font-size: 28px; line-height: 1.2; }
  .contact-rail {
    position: absolute; left: 649px; top: 441px; width: 2px; height: 167px;
    background: var(--brand-orange);
  }
  .contact-list { list-style: none; }
  .contact-item {
    position: absolute; left: 635px;
    display: flex; align-items: flex-start; gap: 27px;
    color: var(--text-light); font-size: 22px; font-weight: 500; line-height: 27px;
  }
  .contact-icon {
    flex: none; width: 30px; height: 30px; border-radius: 50%;
    background: var(--brand-yellow);
    display: flex; align-items: center; justify-content: center;
  }
  .contact-icon svg { width: 18px; height: 18px; }
  .item-address { top: 426px; }
  .item-phone { top: 492px; }
  .item-email { top: 542px; }
  .item-web { top: 593px; }
</style>
</head>
<body>
<div class="card">
  <header class="brand">
    <span class="brand-name">Stonebrook 720</span>
    <span class="brand-mark"></span>
  </header>

  <section class="info-band"></section>

  <div class="name-plate">
    <p class="person-name">Daniel Furlow</p>
    <p class="person-title">Managing Partner</p>
  </div>

  <div class="contact-rail"></div>
  <ul class="contact-list">
    <li class="contact-item item-address">
      <span class="contact-icon">
        <svg viewBox="0 0 24 24" fill="none" stroke="#111" stroke-width="2.2"><path d="M12 21s-6-6.2-6-11a6 6 0 0 1 12 0c0 4.8-6 11-6 11z"/><circle cx="12" cy="10" r="2.2"/></svg>
      </span>
      <span>48317 Whitfield Lane, Suite 510<br>Tampa, FL 33718</span>
    </li>
    <li class="contact-item item-phone">
      <span class="contact-icon">
        <svg viewBox="0 0 24 24" fill="none" stroke="#111" stroke-width="2.2" stroke-linejoin="round"><path d="M5 4h4l2 5-2.5 1.5a11 11 0 0 0 5 5L15 13l5 2v4a2 2 0 0 1-2 2A16 16 0 0 1 3 6a2 2 0 0 1 2-2z"/></svg>
      </span>
      <span>813-555-4870</span>
    </li>
    <li class="contact-item item-email">
      <span class="contact-icon">
        <svg viewBox="0 0 24 24" fill="none" stroke="#111" stroke-width="2.2"><rect x="3" y="6" width="18" height="12" rx="1"/><path d="M3 7l9 6 9-6"/></svg>
      </span>
      <span>dfurlow@stonebrook720.example</span>
    </li>
    <li class="contact-item item-web">
      <span class="contact-icon">
        <svg viewBox="0 0 24 24" fill="none" stroke="#111" stroke-width="2.2"><circle cx="12" cy="12" r="9"/><path d="M3 12h18M12 3c3 3 3 15 0 18M12 3c-3 3-3 15 0 18"/></svg>
      </span>
      <span>www.stonebrook720.example</span>
    </li>
  </ul>
</div>
</body>
</html>
```